New Personal and business business card

I need a new business card design for my business and myslef personally. One side is my business and the other side is my personal information.

Contact Information for Business Card

i will include a copy of my current business card

Colors

Designer to choose colors to be used in the design.

Requirements
Must have
• all of the information currently on my card
Should not have
• i prefer not to have gold color. i know the logo has gold but use gray one

```html
<!DOCTYPE html>
<html lang="en">
<head>
<meta charset="utf-8">
<title>Skyrise Helicopters – Business Card</title>
<link href="https://fonts.googleapis.com/css2?family=Figtree:wght@400;700;800&display=swap" rel="stylesheet">
<style>
  :root {
    --page-bg: #e2e3e5;
    --card-white: #ffffff;
    --card-black: #050607;
    --accent-green: #6fc592;
    --text-dark: #111111;
    --text-grey: #858585;
    --rule-grey: #9a9a9a;
    --bullet-grey: #9c9c9c;
    --text-light: #f2f2f2;
  }
  * { margin: 0; padding: 0; box-sizing: border-box; }
  html, body {
    width: 1200px; height: 1200px; overflow: hidden;
    background: var(--page-bg);
    font-family: "Figtree", sans-serif;
  }
  .canvas { position: relative; width: 1200px; height: 1200px; }

  .card { position: absolute; overflow: hidden; }
  .card-front { left: 181px; top: 43px; width: 851px; height: 536px; background: var(--card-white); }
  .card-back { left: 176px; top: 636px; width: 862px; height: 543px; background: var(--card-black); }
  .base-band { position: absolute; left: 0; right: 0; bottom: 0; background: var(--accent-green); }
  .card-front .base-band { height: 42px; }
  .card-back .base-band { height: 45px; }

  /* Front */
  .brand {
    position: absolute; right: 48px; top: 92px;
    display: flex; align-items: center; gap: 14px;
    font-weight: 800; font-size: 44px; line-height: 1.05; color: var(--text-dark);
    text-align: right;
  }
  .brand-dot { width: 34px; height: 34px; border-radius: 50%; background: var(--text-grey); flex: none; }
  .holder-name {
    position: absolute; left: 46px; top: 217px;
    font-weight: 700; font-size: 37px; color: var(--accent-green); letter-spacing: 0.2px;
  }
  .holder-title {
    position: absolute; left: 46px; top: 258px;
    font-weight: 700; font-size: 22px; color: var(--text-grey);
  }
  .front-rule { position: absolute; left: 46px; top: 300px; width: 760px; height: 3px; background: var(--accent-green); border-radius: 2px; }

  .contact-list { position: absolute; left: 46px; top: 314px; list-style: none; }
  .contact-item { display: flex; align-items: center; height: 38px; font-size: 19px; color: var(--text-dark); }
  .contact-item svg { width: 16px; height: 16px; margin-right: 13px; flex: none; }
  .contact-phone { padding-left: 29px; font-weight: 700; font-size: 23px; margin-top: 2px; }

  .service-list { position: absolute; left: 436px; top: 320px; list-style: none; }
  .service-list li { position: relative; padding-left: 19px; font-size: 20px; line-height: 25.2px; color: var(--text-dark); }
  .service-list li::before {
    content: ""; position: absolute; left: 0; top: 10px;
    width: 7px; height: 7px; border-radius: 50%; background: var(--bullet-grey);
  }

  /* Back */
  .back-name {
    position: absolute; left: 0; right: 0; top: 40px; text-align: center;
    font-weight: 800; font-size: 64px; color: var(--accent-green); letter-spacing: -0.5px;
  }
  .back-rule { position: absolute; left: 46px; top: 110px; width: 770px; height: 4px; background: var(--rule-grey); border-radius: 2px; }
  .credential-list { position: absolute; left: 46px; top: 131px; list-style: none; }
  .credential-list li { position: relative; padding-left: 30px; font-size: 23.5px; height: 46px; line-height: 34px; color: var(--text-light); }
  .credential-list li::before {
    content: ""; position: absolute; left: 0; top: 13px;
    width: 10px; height: 10px; border-radius: 50%; background: var(--accent-green);
  }
</style>
</head>
<body>
<div class="canvas">

  <section class="card card-front">
    <div class="brand"><span class="brand-dot"></span><span>Skyrise<br>Helicopters</span></div>

    <h1 class="holder-name">GARRETT HOLLIS</h1>
    <p class="holder-title">CHIEF PILOT / OWNER</p>
    <div class="front-rule"></div>

    <ul class="contact-list">
      <li class="contact-item">
        <svg viewBox="0 0 16 16" aria-hidden="true"><rect x="1" y="3" width="14" height="10" fill="none" stroke="#9c9c9c" stroke-width="1.4"/><path d="M1 3l7 6 7-6M1 13l5-5M15 13l-5-5" fill="none" stroke="#9c9c9c" stroke-width="1.2"/></svg>
        Garrett.h.Hollis@mailbox.com
      </li>
      <li class="contact-item">
        <svg viewBox="0 0 16 16" aria-hidden="true"><g fill="none" stroke="#9c9c9c" stroke-width="1.1"><circle cx="8" cy="8" r="7"/><ellipse cx="8" cy="8" rx="3" ry="7"/><path d="M1 8h14M2 4.5h12M2 11.5h12"/></g></svg>
        www.skyrisehelicopters.com
      </li>
      <li class="contact-item contact-phone">PH: 555.284.0197</li>
    </ul>

    <ul class="service-list">
      <li>Scenic Tours / Event Rides</li>
      <li>Photography</li>
      <li>Flight Instruction-Airplane &amp; Helicopter</li>
      <li>Special Events</li>
      <li>Frost Patrol / Crop Pollination</li>
      <li>Aircraft Sales</li>
    </ul>

    <div class="base-band"></div>
  </section>

  <section class="card card-back">
    <h2 class="back-name">GARRETT HOLLIS</h2>
    <div class="back-rule"></div>
    <ul class="credential-list">
      <li>Designated Pilot Examiner Rotorcraft Helicopter</li>
      <li>GFII Airplane and Helicopter</li>
      <li>MEI,IGI,AGI</li>
      <li>ATP Multiengine land / ATP Single Engine Land / ATP Helicopter</li>
      <li>Seaplane Instructor</li>
      <li>Marlow Pierce Insurance Check Pilot for Aldridge Helicopters</li>
      <li>Contract Pilot and Instructor</li>
      <li>KX-410s, VR-220 Single Pilot and HM-JET Type Rating</li>
    </ul>
    <div class="base-band"></div>
  </section>

</div>
</body>
</html>
```